Labels for individual cannabis strain names

Looking for a creative label with each strain name and laboratory test information.

Our company is looking for new labels for our new"CO2" oil.

Labels should include each strain name and lab info and say "SUPERCRITICAL CO2 EXTRACT"

Should be able to convert to a foil sticker without losing label quality.

NOTE: Does not need to be a circle-- It can be a square/ rectangle. Label size will be roughly 1.25"X1.0" inches.

Strains:

-Marlo Fizz
THC: 68.65%
CBD: 1.12%
CBN: 1.08 %

-Quillstep
THC: 70.23%
CBD: 1.56%
CBN: 1.64%

-Amber Hush
THC: 68.51%
CBD: 1.19%
CBN: 1.13%

-Kelp Vex
THC: 66.02%
CBD: 1.12%
CBN: 1.56%

-Plimba
THC: 65.11%
CBD:1.35%
CBN: 1.09%

-Otter Drizzle
THC: 65.72%
CBD:1.44%
CBN: 1.09%

-Rumble Tarn
THC: 68.89%
CBD: 1.82%
CBN: 1.09%

-Pebblemoth Zin
THC: 67.01%
CBD: 1.62%
CBN: 1.21%

-Velvet Comet
THC: 66.89%
CBD: 1.91%
CBN: 1.21%

-Dov Palinski
THC: 68.77%
CBD: 1.32%
CBN: 1.16%

-Thistleberry Drift
THC: 67.22%
CBD:1.34%
CBN: 1.12%

-Harbor Moss Wafers
THC: 68.68%
CBD:1.38%
CBN: 1.87%

Industry/Entity Type

It Company

Requirements
Must have
• -"Supercritical CO2 Extract"
• -Strain name, THC, CBD, and CBN testings
• -Brisa Mists horseshoe logo
Nice to have
• A label that will easily convert to a foil sticker without compromising art quality. (example attached)

```html
<!DOCTYPE html>
<html lang="en">
<head>
<meta charset="utf-8">
<title>Supercritical CO2 Extract – Strain Labels</title>
<link rel="stylesheet" href="https://fonts.googleapis.com/css2?family=Jost:wght@400;500;600&display=swap">
<style>
  :root {
    --backdrop: #2b2b2d;
    --gold-light: #fde47a;
    --gold-mid: #f2b91c;
    --gold-deep: #c98a06;
    --silver-light: #ffffff;
    --silver-mid: #e2e2e2;
    --silver-deep: #a9a9a9;
    --star: #f4f4f4;
    --ink: #111111;
    --ink-soft: #2a2a2a;
  }
  html, body {
    margin: 0;
    padding: 0;
    width: 1200px;
    height: 1200px;
    overflow: hidden;
    background: var(--backdrop);
  }
  .label-sheet {
    width: 1200px;
    height: 1200px;
    display: grid;
    grid-template-columns: repeat(4, 260px);
    grid-template-rows: repeat(3, 260px);
    column-gap: 13px;
    row-gap: 36px;
    justify-content: center;
    align-content: center;
  }
  .strain-label {
    width: 260px;
    height: 260px;
    display: block;
  }
  .ring-text {
    font-family: "Jost", sans-serif;
    font-weight: 500;
    font-size: 16.5px;
    letter-spacing: 0.3px;
    fill: var(--ink);
  }
  .strain-name {
    font-family: "Jost", sans-serif;
    font-weight: 500;
    font-size: 22px;
    fill: var(--ink);
    text-anchor: middle;
    dominant-baseline: central;
  }
  .strain-name.is-mid { font-size: 19px; }
  .strain-name.is-long { font-size: 16px; }
  .strain-name.is-longest { font-size: 12.5px; }
  .lab-result {
    font-family: "Jost", sans-serif;
    font-weight: 400;
    font-size: 16px;
    fill: var(--ink-soft);
    text-anchor: middle;
  }
  .defs-holder { position: absolute; width: 0; height: 0; }
</style>
</head>
<body>

<svg class="defs-holder" aria-hidden="true">
  <defs>
    <linearGradient id="gold-ring" x1="0" y1="0" x2="0" y2="1">
      <stop offset="0" stop-color="var(--gold-mid)"/>
      <stop offset="0.5" stop-color="var(--gold-light)"/>
      <stop offset="1" stop-color="var(--gold-mid)"/>
    </linearGradient>
    <linearGradient id="gold-band" x1="0" y1="0" x2="0" y2="1">
      <stop offset="0" stop-color="var(--gold-deep)"/>
      <stop offset="0.35" stop-color="var(--gold-light)"/>
      <stop offset="1" stop-color="var(--gold-mid)"/>
    </linearGradient>
    <radialGradient id="silver-face" cx="0.5" cy="0.5" r="0.5">
      <stop offset="0" stop-color="var(--silver-light)"/>
      <stop offset="0.75" stop-color="var(--silver-mid)"/>
      <stop offset="1" stop-color="var(--silver-deep)"/>
    </radialGradient>
    <linearGradient id="silver-rim" x1="0" y1="0" x2="1" y2="1">
      <stop offset="0" stop-color="#f4f4f4"/>
      <stop offset="1" stop-color="#8d8d8d"/>
    </linearGradient>
    <path id="ring-path" d="M 26,130 A 104,104 0 1 1 234,130 A 104,104 0 1 1 26,130"/>
    <path id="ring-star" d="M0,-5 L1.2,-1.6 L4.8,-1.6 L1.9,0.6 L3,4 L0,1.9 L-3,4 L-1.9,0.6 L-4.8,-1.6 L-1.2,-1.6 Z"/>
    <g id="label-base">
      <circle cx="130" cy="130" r="129" fill="url(#silver-rim)"/>
      <circle cx="130" cy="130" r="126" fill="url(#gold-ring)"/>
      <circle cx="130" cy="130" r="93" fill="var(--silver-deep)"/>
      <circle cx="130" cy="130" r="91" fill="url(#silver-face)" role="img" aria-label="Silver radiating face of the seal"/>
      <text class="ring-text"><textPath href="#ring-path" startOffset="25%" text-anchor="middle">SUPERCRITICAL CO2 EXTRACT</textPath></text>
      <text class="ring-text"><textPath href="#ring-path" startOffset="75%" text-anchor="middle">SUPERCRITICAL CO2 EXTRACT</textPath></text>
      <use href="#ring-star" x="20" y="130" fill="var(--star)"/>
      <use href="#ring-star" x="240" y="130" fill="var(--star)"/>
      <rect x="56" y="76" width="148" height="36" fill="url(#gold-band)"/>
    </g>
  </defs>
</svg>

<main class="label-sheet">

  <svg class="strain-label" viewBox="0 0 260 260" aria-label="Marlo Fizz label">
    <use href="#label-base"/>
    <text class="strain-name" x="130" y="95">MARLO FIZZ</text>
    <text class="lab-result" x="130" y="141">THC: 68.65%</text>
    <text class="lab-result" x="130" y="162">CBD: 1.12%</text>
    <text class="lab-result" x="130" y="183">CBN: 1.08 %</text>
  </svg>

  <svg class="strain-label" viewBox="0 0 260 260" aria-label="Quillstep label">
    <use href="#label-base"/>
    <text class="strain-name" x="130" y="95">QUILLSTEP</text>
    <text class="lab-result" x="130" y="141">THC: 70.23%</text>
    <text class="lab-result" x="130" y="162">CBD: 1.56%</text>
    <text class="lab-result" x="130" y="183">CBN: 1.64%</text>
  </svg>

  <svg class="strain-label" viewBox="0 0 260 260" aria-label="Amber Hush label">
    <use href="#label-base"/>
    <text class="strain-name" x="130" y="95">AMBER HUSH</text>
    <text class="lab-result" x="130" y="141">THC: 68.51%</text>
    <text class="lab-result" x="130" y="162">CBD: 1.19%</text>
    <text class="lab-result" x="130" y="183">CBN: 1.13%</text>
  </svg>

  <svg class="strain-label" viewBox="0 0 260 260" aria-label="Kelp Vex label">
    <use href="#label-base"/>
    <text class="strain-name" x="130" y="95">KELP VEX</text>
    <text class="lab-result" x="130" y="141">THC: 66.02%</text>
    <text class="lab-result" x="130" y="162">CBD: 1.12%</text>
    <text class="lab-result" x="130" y="183">CBN: 1.56%</text>
  </svg>

  <svg class="strain-label" viewBox="0 0 260 260" aria-label="Plimba label">
    <use href="#label-base"/>
    <text class="strain-name" x="130" y="95">PLIMBA</text>
    <text class="lab-result" x="130" y="141">THC: 65.11%</text>
    <text class="lab-result" x="130" y="162">CBD:1.35%</text>
    <text class="lab-result" x="130" y="183">CBN: 1.09%</text>
  </svg>

  <svg class="strain-label" viewBox="0 0 260 260" aria-label="Otter Drizzle label">
    <use href="#label-base"/>
    <text class="strain-name is-long" x="130" y="95">OTTER DRIZZLE</text>
    <text class="lab-result" x="130" y="141">THC: 65.72%</text>
    <text class="lab-result" x="130" y="162">CBD:1.44%</text>
    <text class="lab-result" x="130" y="183">CBN: 1.09%</text>
  </svg>

  <svg class="strain-label" viewBox="0 0 260 260" aria-label="Rumble Tarn label">
    <use href="#label-base"/>
    <text class="strain-name is-mid" x="130" y="95">RUMBLE TARN</text>
    <text class="lab-result" x="130" y="141">THC: 68.89%</text>
    <text class="lab-result" x="130" y="162">CBD: 1.82%</text>
    <text class="lab-result" x="130" y="183">CBN: 1.09%</text>
  </svg>

  <svg class="strain-label" viewBox="0 0 260 260" aria-label="Pebblemoth Zin label">
    <use href="#label-base"/>
    <text class="strain-name is-long" x="130" y="95">PEBBLEMOTH ZIN</text>
    <text class="lab-result" x="130" y="141">THC: 67.01%</text>
    <text class="lab-result" x="130" y="162">CBD: 1.62%</text>
    <text class="lab-result" x="130" y="183">CBN: 1.21%</text>
  </svg>

  <svg class="strain-label" viewBox="0 0 260 260" aria-label="Velvet Comet label">
    <use href="#label-base"/>
    <text class="strain-name is-mid" x="130" y="95">VELVET COMET</text>
    <text class="lab-result" x="130" y="141">THC: 66.89%</text>
    <text class="lab-result" x="130" y="162">CBD: 1.91%</text>
    <text class="lab-result" x="130" y="183">CBN: 1.21%</text>
  </svg>

  <svg class="strain-label" viewBox="0 0 260 260" aria-label="Dov Palinski label">
    <use href="#label-base"/>
    <text class="strain-name is-mid" x="130" y="95">DOV PALINSKI</text>
    <text class="lab-result" x="130" y="141">THC: 68.77%</text>
    <text class="lab-result" x="130" y="162">CBD: 1.32%</text>
    <text class="lab-result" x="130" y="183">CBN: 1.16%</text>
  </svg>

  <svg class="strain-label" viewBox="0 0 260 260" aria-label="Thistleberry Drift label">
    <use href="#label-base"/>
    <text class="strain-name is-longest" x="130" y="95">THISTLEBERRY DRIFT</text>
    <text class="lab-result" x="130" y="141">THC: 67.22%</text>
    <text class="lab-result" x="130" y="162">CBD:1.34%</text>
    <text class="lab-result" x="130" y="183">CBN: 1.12%</text>
  </svg>

  <svg class="strain-label" viewBox="0 0 260 260" aria-label="Harbor Moss Wafers label">
    <use href="#label-base"/>
    <text class="strain-name is-longest" x="130" y="95">HARBOR MOSS WAFERS</text>
    <text class="lab-result" x="130" y="141">THC: 68.68%</text>
    <text class="lab-result" x="130" y="162">CBD:1.38%</text>
    <text class="lab-result" x="130" y="183">CBN: 1.87%</text>
  </svg>

</main>
</body>
</html>
```